Movix3 24/7 Gym & Health Bar Webpage

We need a professional and interactive webpage for a 24/7 health club.
Our approach is professional yet friendly offering holitic professional services for both general and special populations, along with flexible 24/7 gym and group fitness memberships. Professional services that we offer;
Exercise Physiologist
Strength & Conditioning
Physiotherapy
Chiropractor
Nutrition
Personal Training
we also service acute and chronic injuries, work cover, and veteran affairs

We also have a well-being bar offers healthy food, beverages and wide range of supplements.
We send out regular newsletters and want it to be interactive with social media and e-commerce.
Final design should demonstrate a holistic approach where clients have access to a wide range of health services within a professional health club environment. needs to be phone and table friendly please

i have attached a template i had been working on but wasn't happy with it

Target Market(s)

wide demographic including:

Special population - older demographic looking for professional services. Doctors will be referring clients to us also

24/7 gym - aged 25+ yrs, male and female

Industry/Entity Type

Health And Wellness

Coding

Coded - Design and coding required

Number of Pages Required

5+ page

Colors
33a6d7
add136
ffffff
0355a3

Requirements
Must have
• atmosphere and professionalism whilst inviting and sincere
• social media interaction & blog page
• clear navigation
• mobile and table friendly
• Tidal E-newsletter sign up
• testimonials
Nice to have
• customer feedback option
• FAQ
• opportunity to integrate online shop
• ability to download free visit pass

```html
<!DOCTYPE html>
<html lang="en">
<head>
<meta charset="utf-8">
<title>Movix3 24/7 Gym &amp; Health Bar</title>
<link rel="stylesheet" href="https://fonts.googleapis.com/css2?family=Open+Sans:wght@400;600;700&family=Roboto+Condensed:wght@300;400;700&display=swap">
<style>
:root{
  --teal:#33a6d7;
  --green:#add136;
  --btn-green:#6fbe2c;
  --navy:#0355a3;
  --white:#ffffff;
  --ink:#1e1e1e;
  --nav:#6f6f6f;
  --dark:#262626;
}
*{box-sizing:border-box;margin:0;padding:0}
html,body{width:1200px;height:3000px;overflow:hidden;background:var(--white)}
body{position:relative;font-family:"Open Sans",Arial,sans-serif;color:var(--ink)}
.abs{position:absolute}

/* header */
.site-header{left:0;top:0;width:1200px;height:150px;background:var(--white)}
.brand-name{left:48px;top:34px;font-family:"Roboto Condensed",sans-serif;font-weight:400;font-size:60px;line-height:1;color:var(--navy);letter-spacing:1px}
.brand-line{left:50px;top:106px;font-size:13px;font-weight:400;color:var(--nav);letter-spacing:1px}
.follow-top{right:48px;top:14px;display:flex;align-items:center;gap:6px;font-size:12px;color:var(--nav)}
.follow-top span{width:16px;height:16px;border-radius:50%;background:var(--teal);display:inline-block}
.follow-top b{font-weight:400;margin-right:8px}
.main-nav{right:48px;top:62px;display:flex;gap:30px;font-family:"Roboto Condensed",sans-serif;font-size:17px;color:var(--nav)}
.main-nav a{color:inherit;text-decoration:none;position:relative}
.main-nav .current{color:#444}
.main-nav .has-sub::after{content:"";position:absolute;left:50%;top:26px;width:6px;height:6px;margin-left:-3px;border-right:1.5px solid var(--nav);border-bottom:1.5px solid var(--nav);transform:rotate(45deg)}
.nav-underline{left:688px;top:146px;width:72px;height:4px;background:var(--btn-green)}

/* hero */
.hero{left:0;top:150px;width:1200px;height:570px;background:radial-gradient(ellipse at 55% 35%,#5a5a5a 0%,#2e2e2e 45%,#0f0f0f 100%)}
.hero-title{left:0;top:360px;width:1200px;text-align:center;font-family:"Roboto Condensed",sans-serif;font-weight:400;font-size:52px;line-height:72px;color:var(--white);letter-spacing:1px}
.hero-cta{left:508px;top:524px;width:184px;height:44px;background:var(--teal);color:var(--white);font-size:17px;display:flex;align-items:center;justify-content:center}
.hero-dots{left:1138px;top:388px;display:flex;flex-direction:column;gap:8px}
.hero-dots i{width:8px;height:8px;border-radius:50%;background:var(--white);display:block}

/* program tiles */
.program-tiles{left:48px;top:682px;width:1104px;height:200px;display:flex}
.tile{position:relative;flex:1;height:200px}
.tile-a{background:linear-gradient(135deg,#2b7e93,#4fa7b8 60%,#23606e)}
.tile-b{background:linear-gradient(135deg,#3b4b50,#6d7a7d 55%,#2e3a3d)}
.tile-c{background:linear-gradient(135deg,#4a8f8a,#8fb8b2 55%,#3c6e6a)}
.tile-label{position:absolute;left:0;right:0;top:74px;height:42px;display:flex;align-items:center;justify-content:center;font-family:"Roboto Condensed",sans-serif;font-size:25px;color:var(--white);letter-spacing:.5px}
.tile-a .tile-label{background:rgba(51,166,215,.75)}
.tile-b .tile-label{background:rgba(111,190,44,.85)}
.tile-c .tile-label{background:rgba(51,166,215,.6)}

/* section headings */
.section-title{left:0;width:1200px;text-align:center;font-family:"Roboto Condensed",sans-serif;font-weight:300;font-size:60px;color:var(--ink);letter-spacing:1px}
.section-intro{left:220px;width:760px;text-align:center;font-size:13px;line-height:17px;color:#333}

/* service cards */
.service{width:322px}
.service-photo{display:block;width:322px;height:230px}
.service-title{margin-top:14px;font-size:25px;font-weight:400;color:var(--ink);line-height:34px;letter-spacing:-.5px;white-space:nowrap}
.service-text{margin-top:6px;height:45px;font-size:12px;line-height:15px;color:#333}
.learn-more{margin-top:10px;width:92px;height:34px;background:var(--btn-green);color:var(--white);font-size:12px;display:flex;align-items:center;justify-content:center}

/* testimonial */
.testimonial{left:0;top:1965px;width:1200px;height:315px;background:linear-gradient(180deg,#3a3a3a,#1f1f1f 60%,#2b2b2b)}
.testimonial-name{left:0;top:2048px;width:1200px;text-align:center;font-family:"Roboto Condensed",sans-serif;font-size:19px;letter-spacing:4px;color:#ddd}
.testimonial-quote{left:0;top:2074px;width:1200px;text-align:center;font-family:"Roboto Condensed",sans-serif;font-weight:300;font-size:56px;color:var(--white);line-height:70px}
.testimonial-quote .mark{font-size:72px;vertical-align:-8px}
.feedback-btn{left:512px;top:2144px;width:176px;height:42px;background:var(--white);color:var(--ink);font-size:17px;display:flex;align-items:center;justify-content:center}

/* team */
.team-photo{top:2450px;height:190px}
.trainer-card{left:440px;top:2450px;width:320px;height:190px;background:linear-gradient(160deg,#c8e05a,#9dc62e);display:flex;flex-direction:column;align-items:center;justify-content:center;color:var(--white)}
.trainer-role{font-family:"Roboto Condensed",sans-serif;font-size:16px;letter-spacing:4px}
.trainer-name{font-family:"Roboto Condensed",sans-serif;font-size:38px;line-height:42px;letter-spacing:1px}
.trainer-social{display:flex;gap:6px;margin-top:6px}
.trainer-social i{width:14px;height:14px;border-radius:50%;background:var(--white);display:block}

/* footer */
.footer-curve{left:0;top:2620px;width:1200px;height:80px}
.site-footer{left:0;top:2690px;width:1200px;height:295px;background:var(--dark)}
.footer-col{top:2718px;color:var(--white)}
.footer-col h3{font-family:"Roboto Condensed",sans-serif;font-weight:400;font-size:23px;letter-spacing:.5px;margin-bottom:10px}
.footer-col ul{list-style:none;font-size:14px;font-weight:700;line-height:24px}
.newsletter-field{width:236px;height:46px;border:2px solid var(--white);display:flex;align-items:center;gap:12px;padding-left:14px;font-size:13px;color:#ddd}
.subscribe-btn{margin-top:16px;width:124px;height:28px;background:var(--white);color:var(--ink);font-size:14px;display:flex;align-items:center;justify-content:center}
.footer-follow{margin-top:14px;font-family:"Roboto Condensed",sans-serif;font-size:23px}
.footer-social{display:flex;gap:6px;margin-top:8px}
.footer-social i{width:20px;height:20px;border-radius:50%;background:var(--white);display:block}
.copyright-bar{left:0;top:2985px;width:1200px;height:15px;background:var(--white)}
.copyright{right:50px;top:2986px;font-size:11px;color:#333}
</style>
</head>
<body>

<header class="site-header abs">
  <div class="brand-name abs">Movix3</div>
  <div class="brand-line abs">24/7 GYM &amp; HEALTH BAR</div>
  <div class="follow-top abs"><b>FOLLOW US</b><span></span><span></span><span></span><span></span></div>
  <nav class="main-nav abs">
    <a class="current">HOME</a><a class="has-sub">SHOP</a><a>CLASSES</a><a>TRAINERS</a><a>BLOG</a><a>CONTACT</a>
  </nav>
  <div class="nav-underline abs"></div>
</header>

<section class="hero abs" role="img" aria-label="Athlete gripping a loaded barbell in a dark gym with chalk dust"></section>
<h1 class="hero-title abs">THE BEST ONE-HOUR WORKOUT<br>IN THE COUNTRY</h1>
<div class="hero-cta abs">Free visit pass</div>
<div class="hero-dots abs"><i></i><i></i><i></i></div>

<div class="program-tiles abs">
  <div class="tile tile-a" role="img" aria-label="Group fitness class on exercise bikes"><div class="tile-label">FITNESS CLASSES</div></div>
  <div class="tile tile-b" role="img" aria-label="Rack of dumbbells"><div class="tile-label">BODYBUILDING SESSIONS</div></div>
  <div class="tile tile-c" role="img" aria-label="Woman training with a kettlebell"><div class="tile-label">POWER FITNESS</div></div>
</div>

<h2 class="section-title abs" style="top:920px">LET'S TALK ABOUT US</h2>
<p class="section-intro abs" style="top:992px">We are a round-the-clock health club bringing trainers, therapists and nutrition experts under one roof. Whether you are recovering from injury, referred by your doctor or chasing a new personal best, our team builds a plan around you and stays beside you at every step.</p>

<article class="service abs" style="left:48px;top:1085px">
  <div class="service-photo" role="img" aria-label="Dumbbells on a rack in low light" style="background:linear-gradient(135deg,#0c0c0c,#4a4a4a 55%,#111)"></div>
  <h3 class="service-title">Exercise Physiologist</h3>
  <p class="service-text">Clinical exercise plans for chronic conditions, injury recovery and doctor referrals, guided by accredited physiologists.</p>
  <div class="learn-more">Learn More</div>
</article>
<article class="service abs" style="left:440px;top:1085px">
  <div class="service-photo" role="img" aria-label="Runner's feet on a treadmill" style="background:linear-gradient(135deg,#6d6d6d,#cfcfcf 50%,#3a3a3a)"></div>
  <h3 class="service-title">Strength &amp; Conditioning</h3>
  <p class="service-text">Programs that build power, speed and resilience for athletes and members, tracked week by week with clear goals.</p>
  <div class="learn-more">Learn More</div>
</article>
<article class="service abs" style="left:830px;top:1085px">
  <div class="service-photo" role="img" aria-label="Gym floor lined with weight machines" style="background:linear-gradient(135deg,#8a7a6a,#d8cfc4 50%,#5a4e44)"></div>
  <h3 class="service-title">Physiotherapy</h3>
  <p class="service-text">Hands-on treatment for acute and chronic injuries, work cover and veteran affairs clients, next to the gym floor.</p>
  <div class="learn-more">Learn More</div>
</article>

<article class="service abs" style="left:48px;top:1500px">
  <div class="service-photo" role="img" aria-label="Runner silhouetted against an orange sunset" style="background:linear-gradient(160deg,#f6c24a,#e08a1e 55%,#6a3a10)"></div>
  <h3 class="service-title">Chiropractor</h3>
  <p class="service-text">Gentle spinal and joint care that eases pain, restores movement and keeps your training on track all year long.</p>
  <div class="learn-more">Learn More</div>
</article>
<article class="service abs" style="left:440px;top:1500px">
  <div class="service-photo" role="img" aria-label="Cyclist's shoe clipped into a spin bike pedal" style="background:linear-gradient(135deg,#2a2a2a,#bdbdbd 55%,#4a4a4a)"></div>
  <h3 class="service-title">Nutrition</h3>
  <p class="service-text">Meal plans, body composition checks and supplement advice, plus fresh food and drinks from our well-being bar.</p>
  <div class="learn-more">Learn More</div>
</article>
<article class="service abs" style="left:830px;top:1500px">
  <div class="service-photo" role="img" aria-label="Athlete lifting a heavy sandbag in a gym" style="background:linear-gradient(135deg,#3a3430,#8a7a68 55%,#2a2420)"></div>
  <h3 class="service-title">Personal Training</h3>
  <p class="service-text">One-on-one sessions with a coach who learns your goals, sets the pace and pushes you further every visit.</p>
  <div class="learn-more">Learn More</div>
</article>

<section class="testimonial abs" role="img" aria-label="Indoor cycling class in a dim studio"></section>
<div class="testimonial-name abs">JORDAN PELL, NY</div>
<blockquote class="testimonial-quote abs"><span class="mark">&ldquo;</span> TRAINERS PUSH YOU TO YOUR MAX <span class="mark">&rdquo;</span></blockquote>
<div class="feedback-btn abs">ADD FEEDBACK</div>

<h2 class="section-title abs" style="top:2305px">OUR TEAM</h2>
<p class="section-intro abs" style="top:2380px;left:300px;width:600px">Meet the coaches, therapists and specialists who make every session count, day or night, seven days a week.</p>

<div class="team-photo abs" style="left:48px;width:320px;background:linear-gradient(135deg,#1a1a1a,#8a3a2a 50%,#c44a3a)" role="img" aria-label="Smiling trainer in a red top"></div>
<div class="trainer-card abs" role="img" aria-label="Trainer portrait with green overlay">
  <div class="trainer-role">TRAINER</div>
  <div class="trainer-name">MIA CORRAN</div>
  <div class="trainer-social"><i></i><i></i><i></i></div>
</div>
<div class="team-photo abs" style="left:830px;width:320px;background:linear-gradient(135deg,#2a2a2a,#8a6a50 50%,#3a3028)" role="img" aria-label="Muscular trainer posing in the gym"></div>

<svg class="footer-curve abs" viewBox="0 0 1200 80" preserveAspectRatio="none" aria-hidden="true">
  <path d="M0 40 Q600 10 1200 0 L1200 80 L0 80 Z" fill="var(--btn-green)"/>
  <path d="M0 60 Q600 28 1200 14 L1200 80 L0 80 Z" fill="var(--dark)"/>
</svg>
<footer class="site-footer abs"></footer>

<div class="footer-col abs" style="left:48px">
  <h3>OVERVIEW</h3>
  <ul><li>E-store</li><li>Blog</li><li>Gallery</li><li>About us</li><li>Contact</li><li>Guiding tips</li><li>Classes</li></ul>
</div>
<div class="footer-col abs" style="left:270px">
  <h3>PARTNERS</h3>
  <ul><li>E-store</li><li>Blog</li><li>Gallery</li><li>About us</li><li>Contact</li><li>Guiding tips</li><li>Classes</li></ul>
</div>
<div class="footer-col abs" style="left:470px">
  <h3>RECENT NEWS</h3>
  <ul><li>E-store</li><li>Blog</li><li>Gallery</li><li>About us</li><li>Contact</li><li>Guiding tips</li><li>Classes</li></ul>
</div>
<div class="footer-col abs" style="left:690px">
  <h3>RECENT NEWS</h3>
  <ul><li>E-store</li><li>Blog</li><li>Gallery</li><li>About us</li><li>Contact</li><li>Guiding tips</li><li>Classes</li></ul>
</div>
<div class="footer-col abs" style="left:915px">
  <h3>NEWSLETTER</h3>
  <div class="newsletter-field">
    <svg width="18" height="16" viewBox="0 0 18 16" aria-hidden="true"><path d="M1 8 L17 1 L12 15 L9 9 Z" fill="var(--white)"/></svg>
    Enter email address...
  </div>
  <div class="subscribe-btn">Subscribe</div>
  <div class="footer-follow">FOLLOW US</div>
  <div class="footer-social"><i></i><i></i><i></i><i></i><i></i><i></i><i></i></div>
</div>

<div class="copyright-bar abs"></div>
<div class="copyright abs">&copy; 2015 MOVIX3 ALL RIGHTS RESERVED</div>

</body>
</html>
```